Brevik Summit Builders

I own a roofing business Brevikroofing.com and I want to get a Facebook page YouTube Chanel Instagram twitter all the platforms I can add my business to

```html
<!DOCTYPE html>
<html lang="en">
<head>
<meta charset="utf-8">
<title>Brevik Summit Builders – Roof Replacement &amp; Repair</title>
<link rel="stylesheet" href="https://fonts.googleapis.com/css2?family=Plus+Jakarta+Sans:wght@700;800&display=swap">
<style>
  :root {
    --bg-light: #f7f7f7;
    --bg-mid: #dcdcdc;
    --brand-blue: #1c2fc2;
    --edge-blue: #2f46b0;
    --cta-red: #d2232a;
    --white: #ffffff;
    --tile-dark: #9c3f22;
    --tile-mid: #c95f3a;
    --tile-light: #e2835a;
    --trim-teal: #1f7d74;
    --trim-dark: #3a3a36;
  }
  html, body {
    margin: 0;
    padding: 0;
    overflow: hidden;
    background: var(--white);
  }
  .banner {
    position: relative;
    width: 1200px;
    height: 457px;
    overflow: hidden;
    background: linear-gradient(180deg, var(--bg-mid) 0%, #ececec 45%, var(--bg-light) 100%);
    font-family: "Plus Jakarta Sans", sans-serif;
  }
  .roof-photo {
    position: absolute;
    inset: 0;
    width: 1200px;
    height: 457px;
  }
  .brand {
    position: absolute;
    left: 30px;
    top: 56px;
    display: flex;
    align-items: center;
    gap: 10px;
  }
  .brand-mark {
    width: 18px;
    height: 18px;
    background: var(--cta-red);
  }
  .brand-name {
    margin: 0;
    font-size: 25px;
    font-weight: 700;
    color: var(--brand-blue);
    letter-spacing: 0.2px;
  }
  .headline {
    position: absolute;
    left: 31px;
    top: 134px;
    margin: 0;
    font-size: 35px;
    font-weight: 800;
    line-height: 45px;
    letter-spacing: -1.5px;
    color: var(--brand-blue);
    text-transform: uppercase;
  }
  .call-button {
    position: absolute;
    left: 30px;
    top: 339px;
    width: 321px;
    height: 72px;
    border-radius: 36px;
    background: var(--cta-red);
    color: var(--white);
    display: flex;
    align-items: center;
    justify-content: center;
    font-size: 30px;
    font-weight: 700;
    letter-spacing: -0.8px;
    text-decoration: none;
  }
</style>
</head>
<body>
<main class="banner">
  <svg class="roof-photo" viewBox="0 0 1200 457">
    <defs>
      <linearGradient id="roofTones" x1="0" y1="0" x2="1" y2="1">
        <stop offset="0" stop-color="var(--tile-light)"/>
        <stop offset="0.35" stop-color="var(--tile-mid)"/>
        <stop offset="0.6" stop-color="var(--tile-light)"/>
        <stop offset="0.85" stop-color="var(--tile-mid)"/>
        <stop offset="1" stop-color="var(--tile-dark)"/>
      </linearGradient>
      <radialGradient id="trimGlow" cx="0.5" cy="0.22" r="0.55">
        <stop offset="0" stop-color="var(--trim-teal)" stop-opacity="0.45"/>
        <stop offset="1" stop-color="var(--trim-teal)" stop-opacity="0"/>
      </radialGradient>
      <linearGradient id="shade" x1="0" y1="0" x2="0" y2="1">
        <stop offset="0" stop-color="var(--trim-dark)" stop-opacity="0"/>
        <stop offset="0.7" stop-color="var(--trim-dark)" stop-opacity="0.1"/>
        <stop offset="1" stop-color="var(--trim-dark)" stop-opacity="0.3"/>
      </linearGradient>
      <clipPath id="photoClip">
        <path d="M648 0 L1200 0 L1200 457 L498 457 L360 312 Q348 298 360 282 Z"/>
      </clipPath>
    </defs>
    <path class="photo-edge" d="M630 0 L346 276 Q332 298 348 318 L480 457 L498 457 L360 312 Q348 298 360 282 L648 0 Z" fill="var(--edge-blue)"/>
    <g class="photo-area" role="img" aria-label="Photo of a terracotta tile roof with teal-framed dormer windows" clip-path="url(#photoClip)">
      <rect x="340" y="0" width="860" height="457" fill="url(#roofTones)"/>
      <rect x="340" y="0" width="860" height="457" fill="url(#trimGlow)"/>
      <rect x="340" y="0" width="860" height="457" fill="url(#shade)"/>
    </g>
  </svg>

  <div class="brand">
    <span class="brand-mark"></span>
    <p class="brand-name">Brevik Summit Builders</p>
  </div>

  <h1 class="headline">#1 Roof Replacement<br>&amp; Repair Services<br>Contractor in<br>Metro St. Louis</h1>

  <a class="call-button" href="tel:5553184420">(555) 318-4420</a>
</main>
</body>
</html>
```